Velnor Herb Company needs a label for a new line

We need a label design for a new product that is an off shoot of Chef Dorna's Grand Pepper Tin Spices. These new spice blends will be mixed into various condiments including but not limited to ketchup, mayonnaise and butter. We really like the new Brisklane Pecan Tuck Pouch. The label has to have the 1)Chef Dorna logo on it, 2) the the name of the product which is, "Stirlets" for ketchups, Stirlets for mayonnaise and Stirlets for Sour Cream, and then underneath that,3) the flavor i.e. Honeyed Curry Sriracha etc. The labels are going to be put on bags similar to the Brisklane Pecan Tuck Pouch. We actually also like their color combinations. We are going to need to have 3 different color combos because their will be 3 different condiments to mix the product into. There will also be 2 different size black bags that the spices will go in. The 2 oz. bag is 4" W x 2 3/8" G x 6 1/2" H and the 4 oz bag is 5 1/8" W x 3 1/8" G x 8 1/8" H. So we need 3 labels that will all be the same, just the color will need to be different and name of the condiment will change.

I have attached a file with our current spice label and a picture of the Brisklane Pecan Pouch that we like.
Updates

Hi Designer, Please note in the attached file there is a small image of our product with our current logo/image of Chef Dorna. Please use this (or use image on our site http://chefdornasgrandpeppertin.example/ ) as a placeholder for the logo until we find a better/higher-res file. We may also get our printer to swap the image when we go into print production. Thanks.

Target Market(s)

Home cooks and foodies. 25 - 45 year olds

Industry/Entity Type

It Company

Font styles to use
Sans Serif

Requirements
Must have
• Chef Dorna's picture and name

```html
<!DOCTYPE html>
<html lang="en">
<head>
<meta charset="utf-8">
<title>Chef Dorna's Grand Pepper Tin – Stirlets Label</title>
<link rel="stylesheet" href="https://fonts.googleapis.com/css2?family=Jost:wght@300;400&family=Oswald:wght@700&family=Tinos&display=swap">
<style>
  :root {
    --ink: #000000;
    --red: #e3170a;
    --red-deep: #c81208;
    --white: #ffffff;
    --phone: #2a0c08;
    --photo-dark: #1c1c1c;
    --photo-mid: #4a4a4a;
  }
  html, body {
    margin: 0;
    padding: 0;
    overflow: hidden;
    background: var(--ink);
  }
  .label {
    position: relative;
    width: 1200px;
    height: 682px;
    background: var(--ink);
    overflow: hidden;
  }
  .brand-title {
    position: absolute;
    left: 63px;
    top: 44px;
    width: 1072px;
    margin: 0;
    font-family: "Jost", sans-serif;
    font-weight: 300;
    font-size: 100px;
    line-height: 1;
    letter-spacing: 8px;
    color: var(--red);
    text-align: center;
    white-space: nowrap;
  }
  .tagline {
    position: absolute;
    left: 63px;
    top: 156px;
    width: 1072px;
    margin: 0;
    font-family: "Tinos", serif;
    font-size: 21px;
    line-height: 1;
    letter-spacing: 3.5px;
    color: var(--red);
    text-align: center;
    white-space: nowrap;
  }
  .rule {
    position: absolute;
    background: var(--red);
  }
  .rule--top { left: 63px; top: 191px; width: 1072px; height: 9px; }
  .rule--product { left: 456px; top: 314px; width: 679px; height: 9px; }

  .chef-card {
    position: absolute;
    left: 63px;
    top: 216px;
    width: 372px;
    height: 412px;
  }
  .chef-photo {
    position: absolute;
    inset: 0 0 69px 0;
    background:
      radial-gradient(ellipse 45% 55% at 50% 75%, #c8241a 0%, rgba(200,36,26,0) 70%),
      radial-gradient(ellipse 60% 60% at 50% 65%, #d9d9d9 0%, rgba(217,217,217,0) 75%),
      linear-gradient(180deg, var(--photo-dark), var(--photo-mid));
  }
  .chef-name {
    position: absolute;
    left: 0;
    bottom: 0;
    width: 372px;
    height: 69px;
    background: var(--red);
    display: flex;
    align-items: center;
    gap: 10px;
    padding-left: 14px;
    box-sizing: border-box;
    font-family: "Jost", sans-serif;
    font-weight: 400;
    font-size: 38px;
    letter-spacing: 2px;
    color: var(--white);
  }
  .chef-name__dot {
    width: 26px;
    height: 26px;
    border-radius: 50%;
    background: var(--white);
  }

  .product-name {
    position: absolute;
    left: 456px;
    top: 206px;
    margin: 0;
    font-family: "Oswald", sans-serif;
    font-weight: 700;
    font-size: 104px;
    line-height: 1.05;
    letter-spacing: 14px;
    color: var(--white);
    white-space: nowrap;
  }
  .variant {
    position: absolute;
    margin: 0;
    font-family: "Jost", sans-serif;
    font-weight: 300;
    font-size: 34px;
    line-height: 1;
    letter-spacing: 3px;
    color: var(--red);
    white-space: nowrap;
  }
  .variant--mayo { left: 456px; top: 358px; }
  .variant--sour { right: 60px; top: 413px; }

  .stripe-graphic {
    position: absolute;
    left: 456px;
    top: 470px;
    width: 691px;
    height: 158px;
    background: linear-gradient(160deg, var(--red) 0%, var(--red-deep) 100%);
  }
  .phone {
    position: absolute;
    left: 804px;
    top: 582px;
    margin: 0;
    font-family: "Jost", sans-serif;
    font-weight: 400;
    font-size: 25px;
    letter-spacing: 2px;
    color: var(--phone);
  }
  .bags {
    position: absolute;
    left: 1043px;
    top: 510px;
    width: 90px;
    height: 104px;
  }
</style>
</head>
<body>
<main class="label">
  <h1 class="brand-title">GRAND PEPPER TIN</h1>
  <p class="tagline">PREMIUM SPICES FOR ALL TYPES OF COOKING</p>
  <div class="rule rule--top"></div>

  <section class="chef-card">
    <div class="chef-photo" role="img" aria-label="Photo of Chef Dorna in chef's whites, cap and red apron, smiling with open hands"></div>
    <div class="chef-name"><span>Chef Dorna's</span><span class="chef-name__dot"></span></div>
  </section>

  <h2 class="product-name">STIRLETS</h2>
  <div class="rule rule--product"></div>
  <p class="variant variant--mayo">STIRLETS FOR MAYONNAISE</p>
  <p class="variant variant--sour">STIRLETS FOR SOUR CREAM</p>

  <div class="stripe-graphic" role="img" aria-label="Decorative red, white and black zigzag stripe graphic"></div>

  <p class="phone">(866) 555-0148</p>

  <svg class="bags" viewBox="0 0 90 104" aria-hidden="true">
    <g fill="none" stroke="var(--white)" stroke-width="4">
      <path d="M44 20 Q44 4 54 4 Q64 4 64 20"/>
      <path d="M12 44 Q12 30 21 30 Q30 30 30 44"/>
    </g>
    <polygon points="36,18 88,18 90,86 40,86" fill="var(--white)"/>
    <polygon points="2,40 42,40 44,104 0,104" fill="var(--white)" stroke="var(--red)" stroke-width="2"/>
  </svg>
</main>
</body>
</html>
```